Event Center Website

We need a new website design for an upscale event center in Reno, Nevada. The building hosts everything from weddings to corporate events to funerals and it competitively more expensive. The overall look and feel is consistent with a Lake Tahoe aesthetic. The current site can be viewed at www.maplehallvenue.com. They are looking for a major upgrade. A sample site they like is www.cedarbluffstay.com. We have new photography available (some attached). The site should be very visual. A site map is attached as well for direction on what elements the site should include as well as labels for navigation. I am looking for a home page and sample interior page. Any questions, let me know. Thanks.
Updates

I have added some photography of the center itself for use rather than stock photography. Thanks!

Target Market(s)

Brides, professionals, high-income

Industry/Entity Type

Building

Requirements
Must have
• See site map

```html
<!DOCTYPE html>
<html lang="en">
<head>
<meta charset="utf-8">
<title>Maple Hall at Willow Ridge</title>
<link href="https://fonts.googleapis.com/css2?family=PT+Sans+Narrow&family=Open+Sans:wght@400&display=swap" rel="stylesheet">
<style>
  :root {
    --cream: #f5ecd4;
    --cream-dark: #ece0c2;
    --brown: #5b2f14;
    --brown-deep: #4a2510;
    --text-dark: #3a2a1e;
    --text-body: #555;
    --footer-bg: #120404;
    --footer-text: #a89a8e;
    --white: #fff;
    --border: #e2d6bc;
  }
  * { box-sizing: border-box; margin: 0; padding: 0; }
  html, body { width: 1200px; height: 968px; overflow: hidden; background: var(--white); }
  body { position: relative; font-family: "Open Sans", sans-serif; }

  .site-header {
    position: absolute; left: 0; top: 0; width: 1200px; height: 102px;
    background: var(--cream);
  }
  .brand {
    position: absolute; left: 98px; top: 27px; height: 56px;
    display: flex; align-items: center; gap: 10px;
    font-family: "PT Sans Narrow", sans-serif; font-size: 28px; color: var(--brown);
  }
  .brand-mark { width: 22px; height: 22px; background: var(--brown); }
  .main-nav {
    position: absolute; top: 46px; left: 336px; right: 97px;
    display: flex; justify-content: space-between;
    font-family: "PT Sans Narrow", sans-serif; font-size: 13.5px; color: var(--text-dark);
    text-transform: uppercase; letter-spacing: 0.1px;
  }

  .hero {
    position: absolute; left: 0; top: 102px; width: 1200px; height: 580px;
    background: radial-gradient(ellipse at 50% 40%, #9bb36a 0%, #6f8a45 35%, #6b4a33 70%, #4a2e1e 100%);
  }
  .hero-arrow {
    position: absolute; top: 283px; width: 41px; height: 41px; border-radius: 50%;
    background: rgba(40,25,20,0.7); border: 1px solid rgba(255,255,255,0.25);
  }
  .hero-arrow svg { position: absolute; left: 12px; top: 11px; }
  .hero-arrow.prev { left: 38px; }
  .hero-arrow.next { left: 1118px; }

  .booking {
    position: absolute; left: 99px; top: 653px; width: 1003px; height: 94px;
    background: var(--cream); border-radius: 3px;
    box-shadow: 0 10px 12px -8px rgba(0,0,0,0.35);
  }
  .booking-title {
    position: absolute; left: 14px; top: 33px;
    font-family: "PT Sans Narrow", sans-serif; font-size: 21px; color: var(--brown-deep);
  }
  .field {
    position: absolute; top: 24px; width: 182px; height: 41px;
    background: var(--white); border: 1px solid var(--border); border-radius: 2px;
    font-size: 12.5px; color: #777; padding: 12px 12px;
  }
  .field svg { position: absolute; right: 12px; top: 14px; }
  .field.arrival { left: 218px; }
  .field.departure { left: 415px; }
  .field.adults { left: 612px; }
  .reserve-btn {
    position: absolute; left: 802px; top: 24px; width: 182px; height: 42px;
    background: var(--brown); color: var(--white); border-radius: 3px;
    font-family: "PT Sans Narrow", sans-serif; font-size: 15.5px;
    display: flex; align-items: center; justify-content: center;
  }

  .welcome { position: absolute; left: 172px; top: 765px; width: 856px; text-align: center; }
  .welcome h1 {
    font-family: "PT Sans Narrow", sans-serif; font-weight: 400; font-size: 31px; color: var(--text-dark);
  }
  .welcome p { margin-top: 10px; font-size: 12.5px; line-height: 20.6px; color: var(--text-body); }

  .site-footer {
    position: absolute; left: 0; top: 905px; width: 1200px; height: 63px;
    background: var(--footer-bg);
    font-family: "PT Sans Narrow", sans-serif; font-size: 12.5px; color: var(--footer-text);
  }
  .copyright { position: absolute; left: 99px; top: 23px; }
  .social { position: absolute; left: 517px; top: 16px; display: flex; gap: 4px; }
  .social span { width: 30px; height: 30px; border-radius: 50%; border: 2px solid #8a7d72; }
  .legal { position: absolute; right: 99px; top: 23px; text-transform: uppercase; }
</style>
</head>
<body>
  <header class="site-header">
    <div class="brand"><span class="brand-mark"></span>Maple Hall</div>
    <nav class="main-nav">
      <span>About Us</span><span>Gallery</span><span>Weddings</span><span>Meetings</span>
      <span>Other Events</span><span>Catering</span><span>Menus</span><span>FAQs</span>
      <span>Testimonials</span><span>Contact</span>
    </nav>
  </header>

  <section class="hero" role="img" aria-label="Wedding sweetheart table with floral arch and pink draped curtains before a large window onto green trees">
    <div class="hero-arrow prev"><svg width="16" height="18" viewBox="0 0 16 18"><path d="M11 2 L4 9 L11 16" fill="none" stroke="#fff" stroke-width="2.5"/></svg></div>
    <div class="hero-arrow next"><svg width="16" height="18" viewBox="0 0 16 18"><path d="M5 2 L12 9 L5 16" fill="none" stroke="#fff" stroke-width="2.5"/></svg></div>
  </section>

  <section class="booking">
    <div class="booking-title">Schedule an Appointment</div>
    <div class="field arrival">Arrival Date
      <svg width="12" height="12" viewBox="0 0 12 12"><rect x="0.5" y="1.5" width="11" height="10" fill="none" stroke="#999"/><rect x="0.5" y="1.5" width="11" height="2.5" fill="#999"/><path d="M3 6h2M7 6h2M3 9h2M7 9h2" stroke="#999"/></svg></div>
    <div class="field departure">Departure Date
      <svg width="12" height="12" viewBox="0 0 12 12"><rect x="0.5" y="1.5" width="11" height="10" fill="none" stroke="#999"/><rect x="0.5" y="1.5" width="11" height="2.5" fill="#999"/><path d="M3 6h2M7 6h2M3 9h2M7 9h2" stroke="#999"/></svg></div>
    <div class="field adults">Adults
      <svg width="12" height="12" viewBox="0 0 12 12"><rect x="0.5" y="1.5" width="11" height="10" fill="none" stroke="#999"/><rect x="0.5" y="1.5" width="11" height="2.5" fill="#999"/><path d="M3 6h2M7 6h2M3 9h2M7 9h2" stroke="#999"/></svg></div>
    <div class="reserve-btn">RESERVE Online</div>
  </section>

  <section class="welcome">
    <h1>Welcome To Maple Hall</h1>
    <p>Maple Hall is an 8,000 square foot dedicated special events center facility with a full kitchen, bar, and outdoor patio. Maple Hall provides the ideal venue for weddings, business meetings, or any other special event. We have a full time kitchen staff and on site planning staff to assist you with all your catering and event planning needs. We offer a unique and private setting to host your event. From the latest audio and visual</p>
  </section>

  <footer class="site-footer">
    <div class="copyright">©2013 - 2014 &nbsp;Maple Hall at Willow Ridge , All Rights Reserved.</div>
    <div class="social"><span></span><span></span><span></span><span></span><span></span></div>
    <div class="legal">Privacy Policy &nbsp;/&nbsp; Careers</div>
  </footer>
</body>
</html>
```